NEW Modern Sleek Business Card for VR Language Startup

Our startup is using VR to lead the next wave of world language education. We need a two-sided business card that introduces the larger organization (Quorvel Language Inc) and our contact info on one side and shows the product, Lumidrasca, on the other side.

Side 1 (contact info)= Quorvel Logo and Contact info (name, title, phone, email)

Side 2 (product)= Lumidrasc logo, text, and website
Text= Culturally Immersive Language Learning Games
Website= www.lumidrasc.example

Target Market(s)

Education, Technology

Contact Information for Business Card

Contact info will be updated upon approval of the design. For now, put this as a placeholder.

Perry Hollins
Founder & CEO
phollins@mailtrove.example
(555)-014-2736

Font styles to use
Other font styles liked:
• Gibson and Century Gothic are the brand fonts

Requirements
Nice to have
• I would love to see cohesion between the design and colors of the two logos. I have attached a few business card designs that I like, so you can get a feel for my preferred style.

```html
<!DOCTYPE html>
<html lang="en">
<head>
<meta charset="UTF-8">
<title>Lumidrasc / Quorvel Language – Business Card</title>
<link href="https://fonts.googleapis.com/css2?family=Montserrat:wght@400;500;600&family=Questrial&display=swap" rel="stylesheet">
<style>
  :root {
    --backdrop: #d4d6d5;
    --card-white: #ffffff;
    --ink: #1d1d22;
    --ink-soft: #3a3a40;
    --orange: #f39a3c;
    --red: #ec2f55;
    --magenta: #c0287a;
    --violet: #6a4fb5;
    --sky: #4cc3ec;
    --shadow: rgba(0, 0, 0, 0.22);
  }
  * { margin: 0; padding: 0; box-sizing: border-box; }
  html, body {
    width: 1200px;
    height: 900px;
    overflow: hidden;
    background: var(--backdrop);
  }
  .sheet {
    width: 1200px;
    height: 900px;
    display: flex;
    flex-direction: column;
    align-items: center;
    justify-content: center;
    gap: 50px;
  }
  .card {
    position: relative;
    width: 680px;
    height: 389px;
    border-radius: 22px;
    overflow: hidden;
    box-shadow: 0 10px 24px var(--shadow);
  }

  /* Product side */
  .card--product {
    background: linear-gradient(160deg, var(--orange) 0%, var(--red) 35%, var(--magenta) 52%, var(--violet) 68%, var(--sky) 92%);
    color: var(--card-white);
  }
  .card--product .texture {
    position: absolute;
    inset: 0;
    background: linear-gradient(135deg, rgba(255,255,255,0.08), rgba(0,0,0,0.06));
  }
  .product-block {
    position: absolute;
    inset: 0;
    display: flex;
    flex-direction: column;
    align-items: center;
    justify-content: center;
  }
  .product-mark {
    display: flex;
    align-items: center;
    gap: 18px;
  }
  .product-mark .dot {
    width: 64px;
    height: 64px;
    border-radius: 50%;
    background: var(--card-white);
    opacity: 0.9;
  }
  .product-name {
    font-family: "Montserrat", sans-serif;
    font-weight: 500;
    font-size: 76px;
    letter-spacing: 0.5px;
    line-height: 1;
  }
  .product-tagline {
    font-family: "Questrial", sans-serif;
    font-size: 21px;
    margin-top: 14px;
    letter-spacing: 0.3px;
  }
  .product-web {
    font-family: "Questrial", sans-serif;
    font-size: 20px;
    margin-top: 44px;
    letter-spacing: 1px;
  }

  /* Contact side */
  .card--contact { background: var(--card-white); }
  .company-mark {
    position: absolute;
    left: 70px;
    top: 210px;
    display: flex;
    align-items: center;
    gap: 14px;
  }
  .company-mark .dot {
    width: 40px;
    height: 40px;
    border-radius: 50%;
    background: var(--red);
  }
  .company-name {
    font-family: "Montserrat", sans-serif;
    font-weight: 600;
    font-size: 44px;
    letter-spacing: 4px;
    color: var(--ink);
  }
  .contact-block {
    position: absolute;
    left: 380px;
    top: 92px;
    font-family: "Montserrat", sans-serif;
  }
  .person-name {
    font-weight: 600;
    font-size: 26px;
    color: var(--red);
  }
  .person-title {
    font-weight: 400;
    font-size: 17px;
    color: var(--ink-soft);
    margin-top: 2px;
  }
  .divider {
    width: 220px;
    height: 2px;
    margin: 22px 0 20px;
    background: linear-gradient(90deg, var(--sky), var(--violet), var(--red), var(--orange));
  }
  .contact-line {
    display: flex;
    align-items: center;
    gap: 10px;
    font-size: 17px;
    color: var(--ink-soft);
    line-height: 1.6;
  }
  .contact-line svg { width: 15px; height: 15px; flex: none; }
</style>
</head>
<body>
  <main class="sheet">
    <section class="card card--product" aria-label="Product side">
      <div class="texture"></div>
      <div class="product-block">
        <div class="product-mark">
          <span class="dot"></span>
          <span class="product-name">Lumidrasc</span>
        </div>
        <p class="product-tagline">Culturally Immersive Language Learning Games</p>
        <p class="product-web">www.lumidrasc.example</p>
      </div>
    </section>

    <section class="card card--contact" aria-label="Contact side">
      <div class="company-mark">
        <span class="dot"></span>
        <span class="company-name">Quorvel</span>
      </div>
      <div class="contact-block">
        <p class="person-name">Perry Hollins</p>
        <p class="person-title">Founder &amp; CEO</p>
        <div class="divider"></div>
        <p class="contact-line">
          <svg viewBox="0 0 16 16" aria-hidden="true"><path d="M4 1.5 L6.5 4.5 L5 6.5 Q6.5 9.5 9.5 11 L11.5 9.5 L14.5 12 L12.5 14.5 Q5 13.5 1.5 4 Z" fill="var(--red)"/></svg>
          (555)-014-2736
        </p>
        <p class="contact-line">
          <svg viewBox="0 0 16 16" aria-hidden="true"><rect x="1.5" y="3.5" width="13" height="9" fill="none" stroke="var(--red)" stroke-width="1.6"/><path d="M1.5 3.5 L8 9 L14.5 3.5" fill="none" stroke="var(--red)" stroke-width="1.6"/></svg>
          phollins@mailtrove.example
        </p>
      </div>
    </section>
  </main>
</body>
</html>
```